Morvela Aesthetic Doctor

I require an elegant, luxurious looking business card for my aesthetic business. I am a doctor and that will set me aside from competitors. I am planning to provide home and spa based treatments to clients with high expectations. I have attached my logo.

```html
<!DOCTYPE html>
<html lang="en">
<head>
<meta charset="utf-8">
<title>Morvela Aesthetic Doctor – Business Card</title>
<link href="https://fonts.googleapis.com/css2?family=Poppins:wght@300;400;500&display=swap" rel="stylesheet">
<style>
  :root{
    --navy:#0d3f7a;
    --sky:#4fb3e6;
    --sky-soft:#8fd0f0;
    --ink:#3a3d42;
    --grey:#8a8d91;
    --ring:#b9bcc0;
    --paper:#ffffff;
    --stage:#232326;
  }
  *{box-sizing:border-box;margin:0;padding:0}
  html,body{width:1200px;height:800px;overflow:hidden;background:var(--stage)}
  body{font-family:'Poppins',sans-serif;position:relative}
  .card{position:absolute;left:300px;width:600px;height:343px;background:var(--paper);border-radius:22px;overflow:hidden;box-shadow:0 12px 30px rgba(0,0,0,.45)}
  .card--front{top:37px}
  .card--back{top:420px}
  .card__art{position:absolute;inset:0;width:100%;height:100%}

  /* front */
  .brand{position:absolute;left:150px;top:118px;display:flex;align-items:center;gap:16px}
  .brand__ring{width:78px;height:78px;border-radius:50%;border:3px solid var(--ring)}
  .brand__name{color:var(--grey);font-weight:300;line-height:1.05;text-transform:uppercase}
  .brand__name .big{display:block;font-size:46px;letter-spacing:6px}
  .brand__name .small{display:block;font-size:17px;letter-spacing:3px}
  .tagline{position:absolute;right:34px;bottom:36px;color:var(--paper);font-size:14px;font-weight:400;letter-spacing:.4px}

  /* back */
  .mark{position:absolute;right:56px;top:28px;width:128px;height:128px;border-radius:50%;border:3px solid var(--ring);display:flex;align-items:center;justify-content:center;color:var(--grey);font-weight:300;font-size:18px;letter-spacing:2px;text-transform:uppercase}
  .person{position:absolute;left:40px;top:118px}
  .person__name{font-size:23px;font-weight:400;color:var(--ink)}
  .person__name .post{font-size:12px;color:var(--sky);margin-left:6px}
  .person__cred{font-size:13px;color:var(--sky);margin-top:2px}
  .contact{position:absolute;left:40px;top:186px;list-style:none;font-size:13px;color:var(--ink)}
  .contact li{display:flex;align-items:center;gap:8px;margin-bottom:4px}
  .contact__icon{width:16px;height:16px;border-radius:50%;background:var(--sky);display:flex;align-items:center;justify-content:center}
  .social{position:absolute;left:300px;top:188px;display:flex;gap:8px}
  .social span{width:18px;height:18px;border-radius:50%;background:var(--sky)}
  .services{position:absolute;left:40px;top:246px;font-size:13px;color:var(--ink);line-height:1.45}
  .website{position:absolute;right:34px;bottom:36px;color:var(--paper);font-size:14px}
</style>
</head>
<body>

<section class="card card--front" aria-label="Card front">
  <svg class="card__art" viewBox="0 0 600 343" preserveAspectRatio="none" aria-hidden="true">
    <path d="M0 0 H470 C330 40 150 70 0 92 Z" fill="var(--navy)"/>
    <path d="M0 112 C180 86 360 46 520 0 H490 C340 40 160 76 0 100 Z" fill="var(--sky)"/>
    <path d="M600 178 C440 250 270 305 150 343 H600 Z" fill="var(--navy)"/>
    <path d="M0 343 H120 C260 300 440 235 600 160 V145 C420 222 220 290 0 318 Z" fill="var(--sky)"/>
  </svg>
  <div class="brand">
    <div class="brand__ring"></div>
    <div class="brand__name"><span class="big">Morvela</span><span class="small">Aesthetic Doctor</span></div>
  </div>
  <p class="tagline">Home and Spa Based Treatments</p>
</section>

<section class="card card--back" aria-label="Card back">
  <svg class="card__art" viewBox="0 0 600 343" preserveAspectRatio="none" aria-hidden="true">
    <path d="M600 185 C450 262 320 310 230 343 H600 Z" fill="var(--navy)"/>
    <path d="M170 343 H205 C320 300 460 240 600 160 V140 C450 225 310 295 170 343 Z" fill="var(--sky)"/>
  </svg>
  <div class="mark">Morvela</div>
  <div class="person">
    <p class="person__name">Dr Elin Varga<span class="post">MRCPCH MD</span></p>
    <p class="person__cred">Australasian Diploma of Aesthetic Medicine</p>
  </div>
  <ul class="contact">
    <li><span class="contact__icon"><svg width="9" height="9" viewBox="0 0 24 24"><path fill="#fff" d="M6.6 10.8a15 15 0 0 0 6.6 6.6l2.2-2.2a1 1 0 0 1 1-.25 11 11 0 0 0 3.6.6 1 1 0 0 1 1 1V20a1 1 0 0 1-1 1A17 17 0 0 1 3 4a1 1 0 0 1 1-1h3.5a1 1 0 0 1 1 1 11 11 0 0 0 .6 3.6 1 1 0 0 1-.25 1z"/></svg></span>0800 555 014</li>
    <li><span class="contact__icon"><svg width="9" height="9" viewBox="0 0 24 24"><path fill="#fff" d="M2 5h20v14H2z"/><path d="M2 5l10 8 10-8" stroke="var(--sky)" stroke-width="2" fill="none"/></svg></span>elin@morvela.co.nz</li>
  </ul>
  <div class="social" aria-label="Social media"><span></span><span></span></div>
  <p class="services">Dermal injectables - Plasma facials - Microneedling<br>Skin boosters - Excessive sweating<br>Home and Spa Based Treatments</p>
  <p class="website">www.morvela.co.nz</p>
</section>

</body>
</html>
```